Silver Heron Construction Services

Create a business card for my business consulting company
Danielle Vesk, Founder and CEO
4816 Alder Brook Way, Ste 100
Denver, CO. 80451
303.782.4190 cell
dvesk@silverheronconst.example
www.silverheronconst.example

Target Market(s)

Private Equity and Construction Companies

Industry/Entity Type

Business / Sales Consulting

Contact Information for Business Card

Tag Line that says "Where The Road To Success Is Always Under Construction"

Requirements
Must have
• Logo on both sides of the card.
Nice to have
• Add tagline to the same side of the card as my name and contact info

```html
<!DOCTYPE html>
<html lang="en">
<head>
<meta charset="utf-8">
<title>Silver Heron Construction Services – Business Card</title>
<link href="https://fonts.googleapis.com/css2?family=Montserrat:wght@400;500;700&display=swap" rel="stylesheet">
<style>
  :root {
    --backdrop: #e4e4e4;
    --card-white: #ffffff;
    --card-black: #161616;
    --ink: #111111;
    --ink-soft: #2a2a2a;
    --divider: #1f2a6b;
    --silver: #cfcfcf;
    --tagline: #e8e8e8;
  }
  * { box-sizing: border-box; margin: 0; padding: 0; }
  html, body { width: 1200px; height: 1108px; overflow: hidden; }
  body {
    position: relative;
    background: var(--backdrop);
    font-family: "Montserrat", Arial, sans-serif;
    color: var(--ink);
  }
  .card {
    position: absolute;
    width: 729px;
    height: 437px;
  }
  .card--front { left: 238px; top: 67px; background: var(--card-white); }
  .card--back  { left: 245px; top: 580px; background: var(--card-black); }

  .brand-mark {
    position: absolute;
    display: flex;
    align-items: center;
    gap: 8px;
    font-weight: 700;
    text-transform: uppercase;
    line-height: 1.15;
  }
  .brand-mark__square { flex: none; background: currentColor; }
  .card--front .brand-mark {
    right: 16px; top: 48px; width: 138px;
    font-size: 11px; color: var(--ink);
  }
  .card--front .brand-mark__square { width: 12px; height: 12px; }
  .card--back .brand-mark {
    left: 0; right: 0; top: 180px;
    justify-content: center;
    font-size: 30px; color: var(--silver);
    gap: 16px;
  }
  .card--back .brand-mark__square { width: 22px; height: 22px; }

  .identity {
    position: absolute;
    right: 422px; top: 225px;
    text-align: right;
  }
  .identity__name { font-size: 27px; font-weight: 700; letter-spacing: 0.2px; line-height: 1.1; }
  .identity__role { font-size: 15px; font-weight: 400; color: var(--ink-soft); margin-top: 2px; }

  .divider {
    position: absolute;
    left: 322px; top: 190px;
    width: 2px; height: 137px;
    background: var(--divider);
  }

  .contact { position: absolute; left: 343px; top: 185px; font-size: 15.5px; color: var(--ink); }
  .contact__row { display: flex; align-items: center; gap: 11px; height: 31px; }
  .contact__icon { width: 16px; height: 16px; flex: none; }
  .address { position: absolute; left: 343px; top: 292px; font-size: 15.5px; line-height: 21px; }

  .tagline {
    position: absolute;
    left: 0; right: 0; top: 382px;
    text-align: center;
    font-size: 15.5px;
    color: var(--tagline);
    letter-spacing: 0.2px;
  }
</style>
</head>
<body>
  <section class="card card--front" aria-label="Card front">
    <div class="brand-mark"><span class="brand-mark__square"></span><span>Silver Heron Construction Services</span></div>

    <div class="identity">
      <h1 class="identity__name">Danielle Vesk</h1>
      <p class="identity__role">Founder and CEO</p>
    </div>

    <div class="divider"></div>

    <div class="contact">
      <div class="contact__row">
        <svg class="contact__icon" viewBox="0 0 16 16" aria-hidden="true"><path d="M1 5c0-2 3-3 7-3s7 1 7 3v1h-3V5H4v1H1z" fill="#111"/><path d="M3 8l2-2h6l2 2v6H3z" fill="#111"/><circle cx="8" cy="10.5" r="1.6" fill="#fff"/></svg>
        <span>303.782.4190</span>
      </div>
      <div class="contact__row">
        <svg class="contact__icon" viewBox="0 0 16 16" aria-hidden="true"><rect x="1" y="3" width="14" height="10" rx="1" fill="#111"/><path d="M1.5 4l6.5 5 6.5-5" fill="none" stroke="#fff" stroke-width="1.2"/></svg>
        <span>dvesk@silverheronconst.example</span>
      </div>
      <div class="contact__row">
        <svg class="contact__icon" viewBox="0 0 16 16" aria-hidden="true"><circle cx="8" cy="8" r="7" fill="#111"/><path d="M8 1v14M1 8h14M3 4h10M3 12h10" stroke="#fff" stroke-width="0.9" fill="none"/><ellipse cx="8" cy="8" rx="3" ry="7" fill="none" stroke="#fff" stroke-width="0.9"/></svg>
        <span>www.silverheronconst.example</span>
      </div>
    </div>

    <address class="address" style="font-style:normal">
      4816 Alder Brook Way, Ste 100<br>
      Denver, CO. 80451
    </address>
  </section>

  <section class="card card--back" aria-label="Card back">
    <div class="brand-mark"><span class="brand-mark__square"></span><span>Silver Heron<br>Construction Services</span></div>
    <p class="tagline">The Road To Success Is Always Under Construction</p>
  </section>
</body>
</html>
```